Real Estate Website

We need a web design for a new site that is focused on real estate listings and information for the Singapore, Malaysian and Australian market.

The web site will have listings of available real estate for sale, past transaction data on real estate, information about neighborhoods where the real estate is located.
Website URL will likely be www.dwellora.net. We are also open to suggestions on site names (assuming URL is available).

We like the simplicity of a similar US site called Vexomi.com - and want to focus on providing a similar "clean" user interface where users can find the information they need. The final design should be user friendly, be visually compelling with a focus on ease of navigation.

Requirements to have at least 5 web pages designed that will display the data as in the attached document for any given territory. We will need to receive
- HTML/CSS/JavaScript, and all images
- any design icons for common objects (e.g. house/home, map, user, agent, trend chart, contact, bathroom, bedroom, garage, furniture, price, ...etc).
Updates

Hi

I just added more details to the brief and committed to pay for the project.
Please review the additional information and submit your final designs by June 14th (or sooner) as we have a deadline to meet. 

Let me know if you have any questions, I will try to be prompt in my responses. 
Thanks.

Target Market(s)

Consumers who are researching real estate to purchase or sell

Industry/Entity Type

Real Estate

Requirements
Must have
• Data in attached document needs to be displayed.

```html
<!DOCTYPE html>
<html lang="en">
<head>
<meta charset="utf-8">
<title>Homvale – Real Estate</title>
<link href="https://fonts.googleapis.com/css2?family=Oswald:wght@400&family=Source+Sans+3:wght@400;600&display=swap" rel="stylesheet">
<style>
  :root{
    --black:#000;
    --bar:#4a4a4a;
    --nav:#4b4b4b;
    --divider:#d8d8d8;
    --panel-outer:#4a4a4a;
    --panel-inner:#b9b9b9;
    --white:#fff;
    --text:#333;
    --rule:#bdbdbd;
    --orange-top:#f7931e;
    --orange-bottom:#f15a24;
  }
  *{box-sizing:border-box;margin:0;padding:0}
  html,body{width:941px;height:1200px;overflow:hidden;background:var(--white)}
  body{position:relative;font-family:"Source Sans 3",sans-serif;color:var(--text)}
  .abs{position:absolute}

  .top-strip{left:0;top:0;width:941px;height:12px;background:var(--bar)}
  .header{left:0;top:12px;width:941px;height:131px;background:var(--black)}
  .brand{left:40px;top:54px;font-family:"Oswald",sans-serif;font-size:38px;color:var(--white);letter-spacing:.5px;line-height:1}
  .site-search{left:655px;top:64px;width:254px;height:34px;border-radius:4px;background:linear-gradient(#5a5a5a,#3e3e3e);color:#eee;font-size:13px;padding:8px 16px}
  .site-search svg{position:absolute;right:10px;top:6px}

  .nav{left:0;top:143px;width:941px;height:33px;background:var(--nav);display:flex}
  .nav a{color:var(--white);text-decoration:none;font-size:12.5px;display:flex;align-items:center;justify-content:center;height:33px;border-right:1px solid var(--divider)}
  .nav a:last-child{border-right:0}

  .hero{left:25px;top:190px;width:898px;height:378px;border:1px solid #ccc;box-shadow:2px 2px 4px rgba(0,0,0,.35);
    background:linear-gradient(180deg,#e9e7e3 0%,#d9dcd8 30%,#8e9691 55%,#a7aca6 75%,#e5e5e2 100%)}

  .finder-outer{left:37px;top:593px;width:867px;height:176px;background:var(--panel-outer)}
  .finder-inner{left:49px;top:607px;width:842px;height:143px;background:var(--panel-inner)}
  .tab{top:634px;font-size:17px;color:#4a4a4a}
  .field{top:677px;height:35px;background:var(--white);border:1px solid #ddd;font-size:12.5px;color:#333;padding:9px 13px}
  .field svg{position:absolute;right:11px;top:12px}
  .btn-search{left:714px;top:677px;width:111px;height:36px;background:linear-gradient(var(--orange-top),var(--orange-bottom));color:var(--white);font-size:17px;text-align:center;line-height:36px;box-shadow:1px 1px 2px rgba(0,0,0,.3)}

  .welcome-title{left:37px;top:788px;font-size:17px;font-weight:400;color:#333}
  .rule{left:39px;width:867px;height:2px;background:var(--rule)}
  .intro{left:40px;top:845px;width:553px;font-size:12px;line-height:21.4px;text-align:justify;color:#333}
  .intro-photo{left:611px;top:847px;width:292px;height:120px;background:linear-gradient(180deg,#3f6a9c 0%,#7ea2c6 40%,#d9d2b8 62%,#c8bd9d 100%)}

  .card{top:1015px;height:74px;background:linear-gradient(var(--orange-top),var(--orange-bottom));color:var(--white)}
  .card-title{position:absolute;top:22px;font-size:22px;line-height:1}
  .card-copy{position:absolute;top:13px;width:173px;font-size:10.5px;line-height:15px}
  .card-copy span{display:block;text-align:justify;text-align-last:justify}
  .card-copy span.last{text-align-last:left}
  .call{left:633px;width:271px}
  .call p{position:absolute;left:23px;top:9px;font-size:22px;line-height:28px}

  .footer{left:0;top:1109px;width:941px;height:91px;background:var(--black)}
  .copyright{left:0;top:1143px;width:920px;text-align:center;color:var(--white);font-size:12.5px}
</style>
</head>
<body>
  <div class="abs top-strip"></div>
  <header class="abs header"></header>
  <div class="abs brand">HOMVALE</div>
  <div class="abs site-search">Search
    <svg width="20" height="20" viewBox="0 0 20 20"><circle cx="8" cy="8" r="6" fill="#8fb6dd" stroke="#dfe8f0" stroke-width="1.5"/><line x1="12.5" y1="12.5" x2="18" y2="18" stroke="#9a9a9a" stroke-width="3" stroke-linecap="round"/></svg>
  </div>

  <nav class="abs nav">
    <a style="width:127px">Home</a>
    <a style="width:140px">About Us</a>
    <a style="width:140px">Buy</a>
    <a style="width:139px">Rent</a>
    <a style="width:141px">Mortgage</a>
    <a style="width:126px">Local Info</a>
    <a style="width:128px">Contact Us</a>
  </nav>

  <div class="abs hero" role="img" aria-label="Photo of a large grey two-storey Victorian house with a white wraparound porch, turret and bare autumn trees"></div>

  <div class="abs finder-outer"></div>
  <div class="abs finder-inner"></div>
  <div class="abs tab" style="left:76px">For Sale</div>
  <div class="abs tab" style="left:169px">For Rent</div>
  <div class="abs tab" style="left:276px">Sold</div>
  <div class="abs tab" style="left:354px">Estimates</div>
  <div class="abs field" style="left:75px;width:388px">New york, Ny</div>
  <div class="abs field" style="left:473px;width:109px">Beds
    <svg width="16" height="10" viewBox="0 0 16 10"><polyline points="1,1 8,8 15,1" fill="none" stroke="#111" stroke-width="2.5"/></svg>
  </div>
  <div class="abs field" style="left:594px;width:109px">Baths
    <svg width="16" height="10" viewBox="0 0 16 10"><polyline points="1,1 8,8 15,1" fill="none" stroke="#111" stroke-width="2.5"/></svg>
  </div>
  <div class="abs btn-search">Search</div>

  <h2 class="abs welcome-title">Welcome to our site</h2>
  <div class="abs rule" style="top:824px"></div>
  <p class="abs intro">Lorem Ipsum is simply dummy text of the printing and typesetting industry. Lorem Ipsum has been the industry's standard dummy text ever since the 1500s, when an unknown printer took a galley of type and scrambled it to make a type specimen book. It has survived not only five centuries, but also the leap into electronic typesetting, remaining essentially unchanged. It was popularised in the 1960s with the release of Typrella sheets containing Lorem Ipsum passages, and more recently with desktop publishing software like Brevis PageForge including versions of Lorem Ipsum.</p>
  <div class="abs intro-photo" role="img" aria-label="Photo of a row of cream townhouses with grey roofs under a blue sky"></div>
  <div class="abs rule" style="top:998px"></div>

  <div class="abs card" style="left:39px;width:271px">
    <span class="card-title" style="left:19px">BUY</span>
    <p class="card-copy" style="left:77px"><span>It is a long established fact that a</span><span>reader will be distracted by the</span><span class="last">readable content of a page</span></p>
  </div>
  <div class="abs card" style="left:332px;width:272px">
    <span class="card-title" style="left:19px">Rent</span>
    <p class="card-copy" style="left:82px"><span>It is a long established fact that a</span><span>reader will be distracted by the</span><span class="last">readable content of a page</span></p>
  </div>
  <div class="abs card call">
    <p>Call Us Now on<br>XXX.XXXX.XXX</p>
  </div>

  <footer class="abs footer"></footer>
  <div class="abs copyright">Copyrights @ 2012 All Rights Reserved</div>
</body>
</html>
```